Fall Convention Graphic Designs (logo, digital brochure, t-shirt designs, social media templates)

I need a graphic package for the Bellrose Motion Guild Fall Dance Convention. Bellrose Motion Guild is a non-profit organization of dance teachers, and this educational dance conference is for members and their students with multiple events throughout the weekend. The convention has a new them each year. I will need a package with a general "logo" type graphic, a digital brochure, t-shirt design, and social media graphic templates. This year's Convention has a general theme and names for each event throughout the weekend.
The theme and event names for this year are:
Convention Theme Twice Around a Tune: Beneath the Harbor Moon
Registration Desk The Compass Nook
Members Welcome A Moonbeam Greeting
Banquet A Velvet Twilight
President's Reception Raise Every Glass
Jr. Member Desk Wanderers' Wharf
Jr. Member Pizza Party Cricket Mixer
Members Luncheon Meadow Reveries

I am attaching a word file that includes information and text to be included in brochure. Also attached are designs from previous years for brochures, T-shirts, and social media graphics.

Colors that we will be using for decorations at various events over the weekend this year are shades of green (fern and mossy green), shades of blue (including navy), white, and pinks (including mauve). The banquet event will be decorated as an enchanted forest. We are using fairy lights, books that look like a storybook, and lanterns for decorations as well. I think I would like a more modern design, and I do not want anything that is childish or too whimsical. While we are using floral decorations I don't want bunches of flowers in the design.

*I am open to seeing initial logo type designs and giving feedback to make sure it is a direction that I like and then moving forward with the other parts of the project.

```html
<!DOCTYPE html>
<html lang="en">
<head>
<meta charset="utf-8">
<title>Bellrose Motion Guild – 2026 Fall Convention Brochure</title>
<link rel="stylesheet" href="https://fonts.googleapis.com/css2?family=Great+Vibes&family=Libre+Baskerville:wght@700&family=Noto+Serif:ital,wght@0,400;0,600;1,400&family=Nunito+Sans:wght@400;600;700&family=Cormorant+Garamond:wght@500&display=swap">
<style>
  :root {
    --page: #ffffff;
    --ink: #ffffff;
    --ink-soft: #e9ece8;
    --mauve: #b8646f;
    --frame: rgba(255,255,255,0.75);
    --forest-deep: #0f120c;
    --forest-mid: #2c2a16;
    --night-deep: #0d1414;
    --night-mid: #24403d;
  }
  * { margin: 0; padding: 0; box-sizing: border-box; }
  html, body { width: 1200px; height: 533px; overflow: hidden; background: var(--page); }
  .canvas { position: relative; width: 1200px; height: 533px; }

  .panel {
    position: absolute; top: 30px; width: 362px; height: 469px;
    overflow: hidden; color: var(--ink); text-align: center;
  }
  .panel--cover { left: 33px; }
  .panel--welcome { left: 423px; }
  .panel--events { left: 813px; }

  .panel__backdrop { position: absolute; inset: 0; }
  .panel--cover .panel__backdrop {
    background:
      radial-gradient(ellipse 45% 35% at 50% 52%, #2f4a25 0%, rgba(47,74,37,0) 100%),
      radial-gradient(ellipse 60% 60% at 50% 40%, var(--forest-mid) 0%, var(--forest-deep) 80%);
  }
  .panel--welcome .panel__backdrop,
  .panel--events .panel__backdrop {
    background:
      radial-gradient(ellipse 30% 12% at 50% 6%, rgba(170,190,190,0.35) 0%, rgba(170,190,190,0) 100%),
      radial-gradient(ellipse 70% 60% at 50% 60%, var(--night-mid) 0%, var(--night-deep) 90%);
  }

  .panel__frame {
    position: absolute; inset: 7px;
    border: 1px solid var(--frame);
    outline: 1px solid var(--frame); outline-offset: -3px;
    pointer-events: none;
  }
  .panel__content { position: absolute; inset: 0; }

  .script { font-family: 'Great Vibes', cursive; font-weight: 400; }
  .sans { font-family: 'Nunito Sans', sans-serif; }
  .serif { font-family: 'Noto Serif', serif; }

  .divider { position: absolute; left: 0; right: 0; display: block; margin: 0 auto; }

  /* Cover */
  .cover__org { position: absolute; top: 43px; left: 0; right: 0; font-family: 'Libre Baskerville', serif; font-size: 14.5px; line-height: 18px; letter-spacing: 0.3px; }
  .cover__mark { position: absolute; top: 74px; left: 0; right: 0; font-family: 'Libre Baskerville', serif; font-weight: 700; font-size: 31px; line-height: 38px; color: var(--ink); }
  .cover__edition { position: absolute; top: 159px; left: 0; right: 0; font-size: 10.5px; line-height: 14px; font-weight: 700; letter-spacing: 1.6px; }
  .cover__date { position: absolute; top: 282px; left: -14px; right: 0; font-family: 'Cormorant Garamond', serif; font-weight: 500; font-size: 17px; line-height: 22px; letter-spacing: 1.2px; }
  .cover__venue { position: absolute; top: 303px; left: -14px; right: 0; font-size: 10.5px; font-weight: 600; letter-spacing: 1px; line-height: 17px; }
  .cover__tagline { position: absolute; top: 387px; left: 0; right: 0; font-size: 10.5px; line-height: 14px; font-weight: 600; letter-spacing: 1px; }
  .cover__chapter { position: absolute; top: 400px; left: 0; right: 0; font-size: 24px; line-height: 30px; }

  /* Welcome */
  .welcome__title { position: absolute; top: 8px; left: 0; right: 0; font-size: 68px; line-height: 80px; color: var(--mauve); }
  .welcome__intro { position: absolute; top: 77px; left: 26px; right: 26px; font-size: 10.8px; line-height: 17px; }
  .welcome__theme { position: absolute; top: 133px; left: 0; right: 0; font-style: italic; font-size: 12.8px; line-height: 18px; }
  .welcome__body { position: absolute; top: 150px; left: 30px; right: 30px; font-size: 10.8px; line-height: 15.4px; }
  .welcome__divider { top: 212px; }
  .welcome__venue-label { position: absolute; top: 246px; left: 0; right: 0; color: var(--mauve); font-weight: 600; font-size: 12px; line-height: 16px; letter-spacing: 0.6px; }
  .welcome__venue-name { position: absolute; left: 0; right: 0; font-weight: 600; font-size: 11.2px; line-height: 16px; }
  .welcome__venue-name--hall { top: 265px; }
  .welcome__venue-name--hotel { top: 282px; }
  .welcome__details { position: absolute; top: 298px; left: 30px; right: 30px; font-size: 9.4px; line-height: 15.3px; }
  .welcome__closing { position: absolute; top: 384px; left: 0; right: 0; font-size: 22px; line-height: 25px; color: var(--mauve); }

  /* Events */
  .events__title { position: absolute; top: 32px; left: 0; right: 0; font-size: 23px; line-height: 28px; }
  .events__divider { top: 62px; }
  .events__list { position: absolute; top: 82px; left: 0; right: 0; list-style: none; }
  .event { height: 45px; }
  .event__name { display: block; font-size: 19.5px; line-height: 22px; }
  .event__role { display: block; font-size: 7.4px; letter-spacing: 0.6px; line-height: 9px; color: var(--ink-soft); }
  .event__kicker { display: block; font-family: 'Cormorant Garamond', serif; font-size: 11.5px; letter-spacing: 0.8px; line-height: 13px; margin-bottom: 2px; }
  .event--theme { height: 63px; }
</style>
</head>
<body>
<main class="canvas">

  <section class="panel panel--cover">
    <div class="panel__backdrop" role="img" aria-label="Photograph of a dark enchanted forest path framed by twisted trees and glowing fairy lights"></div>
    <div class="panel__content">
      <p class="cover__org">Bellrose Motion Guild</p>
      <p class="cover__mark">Twice Around<br>a Tune</p>
      <p class="cover__edition sans">THE 2026 FALL CONVENTION</p>
      <p class="cover__date">NOVEMBER 19 - 22, 2026</p>
      <p class="cover__venue sans">LINDEN HALL CONVENTION CENTER<br>ASHGROVE HARBOR HOTEL<br>MARLOW BAY, NC</p>
      <p class="cover__tagline sans">DANCE INSPIRES</p>
      <p class="cover__chapter script">the Next Chapter</p>
    </div>
    <div class="panel__frame"></div>
  </section>

  <section class="panel panel--welcome">
    <div class="panel__backdrop" role="img" aria-label="Photograph of a misty moonlit pine forest at night"></div>
    <div class="panel__content serif">
      <h1 class="welcome__title script">Welcome</h1>
      <p class="welcome__intro">Join us for an unforgettable weekend of dance, learning, connection and magic at the Bellrose Motion Guild<br>Fall Convention!</p>
      <p class="welcome__theme">Twice Around a Tune: Beneath the Harbor Moon</p>
      <p class="welcome__body"><br>brings our dance community together<br>for inspiring classes, exciting events and cherished traditions.</p>
      <svg class="divider welcome__divider" width="168" height="10" viewBox="0 0 168 10" aria-hidden="true">
        <line x1="0" y1="5" x2="76" y2="5" stroke="var(--mauve)" stroke-width="1"/>
        <line x1="92" y1="5" x2="168" y2="5" stroke="var(--mauve)" stroke-width="1"/>
        <circle cx="84" cy="5" r="2.5" fill="var(--mauve)"/>
      </svg>
      <h2 class="welcome__venue-label">VENUE &amp; HOTEL</h2>
      <p class="welcome__venue-name welcome__venue-name--hall">Linden Hall Convention Center</p>
      <p class="welcome__venue-name welcome__venue-name--hotel">Ashgrove Harbor Hotel</p>
      <p class="welcome__details">4470 Wrenfield Avenue Marlow Bay, NC 28990<br>Call for reservations and mention BMG for your<br>best rate!<br>555-018-4420 or book online.<br>[Insert Link for Room Block]</p>
      <p class="welcome__closing script">We can't wait to see you<br>Beneath the Harbor Moon!</p>
    </div>
    <div class="panel__frame"></div>
  </section>

  <section class="panel panel--events">
    <div class="panel__backdrop" role="img" aria-label="Photograph of a dark misty pine forest under a pale moon"></div>
    <div class="panel__content">
      <h2 class="events__title script">Convention Theme &amp; Events</h2>
      <svg class="divider events__divider" width="140" height="10" viewBox="0 0 140 10" aria-hidden="true">
        <line x1="0" y1="5" x2="62" y2="5" stroke="var(--mauve)" stroke-width="1"/>
        <line x1="78" y1="5" x2="140" y2="5" stroke="var(--mauve)" stroke-width="1"/>
        <circle cx="70" cy="5" r="2.2" fill="var(--mauve)"/>
      </svg>
      <ul class="events__list">
        <li class="event event--theme">
          <span class="event__kicker">TWICE AROUND A TUNE:</span>
          <span class="event__name script">Beneath the Harbor Moon</span>
          <span class="event__role sans">CONVENTION THEME</span>
        </li>
        <li class="event"><span class="event__name script">The Compass Nook</span><span class="event__role sans">REGISTRATION DESK</span></li>
        <li class="event"><span class="event__name script">A Moonbeam Greeting</span><span class="event__role sans">MEMBERS WELCOME</span></li>
        <li class="event"><span class="event__name script">A Velvet Twilight</span><span class="event__role sans">BANQUET</span></li>
        <li class="event"><span class="event__name script">Raise Every Glass</span><span class="event__role sans">PRESIDENT'S RECEPTION</span></li>
        <li class="event"><span class="event__name script">Wanderers' Wharf</span><span class="event__role sans">JR. MEMBER DESK</span></li>
        <li class="event"><span class="event__name script">Cricket Mixer</span><span class="event__role sans">JR. MEMBER PIZZA PARTY</span></li>
        <li class="event"><span class="event__name script">Meadow Reveries</span><span class="event__role sans">MEMBERS LUNCHEON</span></li>
      </ul>
    </div>
    <div class="panel__frame"></div>
  </section>

</main>
</body>
</html>
```